Varnel Supply requires a new business card.

We are an online professional tool store.

Target Market(s)

We target the professional technician.

Industry/Entity Type

Business

Contact Information for Business Card

VarnelSupply.com.au

sales@varnelsupply.example

Requirements
Must have
• Needs to look commercial and professional
Should not have
• No Australian Colors, maps or shapes.
• No Shapes of Tools

```html
<!DOCTYPE html>
<html lang="en">
<head>
<meta charset="utf-8">
<title>Varnel Supply – Business Card</title>
<link href="https://fonts.googleapis.com/css2?family=Montserrat:wght@500;600;700&family=Open+Sans:wght@400;600&display=swap" rel="stylesheet">
<style>
  :root {
    --bg: #e4e6ea;
    --card: #ffffff;
    --brand-blue: #3d4fa3;
    --accent-blue: #2a9fd0;
    --ink: #3a3a3d;
    --grey-band: #6d6e71;
    --divider: #9a9a9a;
  }
  * { margin: 0; padding: 0; box-sizing: border-box; }
  html, body { width: 1200px; height: 900px; overflow: hidden; }
  body {
    background: var(--bg);
    font-family: "Open Sans", sans-serif;
    position: relative;
  }
  .card {
    position: absolute;
    left: 240px;
    width: 720px;
    height: 400px;
    background: var(--card);
    overflow: hidden;
    box-shadow: 0 6px 18px rgba(0,0,0,0.12);
  }
  .card-front { top: 40px; }
  .card-back { top: 460px; }

  .brand {
    display: flex;
    align-items: center;
    gap: 14px;
    font-family: "Montserrat", sans-serif;
    font-weight: 700;
    color: var(--brand-blue);
    white-space: nowrap;
  }
  .brand-dot {
    width: 30px; height: 30px;
    border-radius: 50%;
    background: var(--accent-blue);
    flex: none;
  }
  .card-front .brand {
    position: absolute;
    left: 50%; top: 50%;
    transform: translate(-50%, -50%);
    font-size: 44px;
  }
  .card-back .brand {
    position: absolute;
    left: 60px; top: 128px;
    font-size: 34px;
  }
  .card-back .brand-dot { width: 24px; height: 24px; }

  .divider {
    position: absolute;
    left: 350px; top: 40px;
    width: 1px; height: 230px;
    background: var(--divider);
  }
  .contact {
    position: absolute;
    left: 380px; top: 58px;
    color: var(--ink);
  }
  .person-name {
    font-family: "Montserrat", sans-serif;
    font-weight: 700;
    font-size: 24px;
    line-height: 1.1;
    color: var(--ink);
  }
  .person-title {
    font-size: 15px;
    color: var(--brand-blue);
    margin-bottom: 30px;
  }
  .contact-list { list-style: none; }
  .contact-list li {
    display: flex;
    align-items: center;
    gap: 12px;
    font-size: 18px;
    line-height: 1.55;
  }
  .contact-list svg { width: 18px; height: 18px; flex: none; }
  .phone-number { font-weight: 600; letter-spacing: 0.5px; }

  .band-blue {
    position: absolute;
    left: 0; right: 0; bottom: 0;
    height: 52px;
    background: var(--brand-blue);
  }
  .band-line {
    position: absolute;
    left: 310px; right: 0; bottom: 94px;
    height: 4px;
    background: var(--brand-blue);
  }
  .band-grey {
    position: absolute;
    left: 330px; right: 0; bottom: 0;
    height: 88px;
    background: var(--grey-band);
    border-top-left-radius: 22px;
    border-left: 4px solid #ffffff;
    border-top: 4px solid #ffffff;
  }
  .abn {
    position: absolute;
    right: 40px; top: 16px;
    color: #ffffff;
    font-size: 17px;
    letter-spacing: 0.5px;
  }
</style>
</head>
<body>

  <section class="card card-front" aria-label="Card front">
    <div class="brand"><span class="brand-dot"></span>Varnel Supply</div>
  </section>

  <section class="card card-back" aria-label="Card back">
    <div class="brand"><span class="brand-dot"></span>Varnel Supply</div>

    <div class="divider"></div>

    <div class="contact">
      <p class="person-name">Anton Merrick</p>
      <p class="person-title">Sales Manager</p>
      <ul class="contact-list">
        <li>
          <svg viewBox="0 0 20 20" aria-hidden="true"><rect x="1" y="4" width="18" height="12" rx="1.5" fill="var(--accent-blue)"/><path d="M1.5 5 L10 11 L18.5 5" stroke="#fff" stroke-width="1.6" fill="none"/></svg>
          sales@varnelsupply.example
        </li>
        <li>
          <svg viewBox="0 0 20 20" aria-hidden="true"><circle cx="10" cy="10" r="8.5" fill="none" stroke="var(--accent-blue)" stroke-width="1.6"/><ellipse cx="10" cy="10" rx="3.5" ry="8.5" fill="none" stroke="var(--accent-blue)" stroke-width="1.4"/><path d="M1.5 10 H18.5" stroke="var(--accent-blue)" stroke-width="1.4"/></svg>
          www.VarnelSupply.com.au
        </li>
        <li>
          <svg viewBox="0 0 20 20" aria-hidden="true"><rect x="5" y="1.5" width="10" height="17" rx="2" fill="none" stroke="var(--accent-blue)" stroke-width="1.6"/><rect x="7" y="4" width="6" height="8" fill="var(--accent-blue)"/><circle cx="10" cy="15.5" r="1" fill="var(--accent-blue)"/></svg>
          <span class="phone-number">0400 555 017</span>
        </li>
      </ul>
    </div>

    <div class="band-blue"></div>
    <div class="band-line"></div>
    <div class="band-grey">
      <span class="abn">ABN 51824093617</span>
    </div>
  </section>

</body>
</html>
```